Business Card Design Project

We need a Business Card for an Mechanical Engineering firm in Singapore. The design should be Modern & Technical looking, yet eye catching.

Our company deals in Cutting Tools & Machine Accessories for the Manufacturing Industries such as Oil & Gas, Aero Space, etc... For more information on our Company, you can either email me or view our website www.valtrion.com.sg.

We are trying to revamp our image to give our consumers a fresh new perspective to our company, so we welcome all ideas.

Industry/Entity Type

Business

Requirements
Must have
• Must incorporate New Company Logo into the card as shown in Uploaded file.

```html
<!DOCTYPE html>
<html lang="en">
<head>
<meta charset="utf-8">
<title>Valtrion Tools – Business Card</title>
<link rel="stylesheet" href="https://fonts.googleapis.com/css2?family=Jura:wght@400;500&display=swap">
<style>
  :root {
    --page-bg: #ffffff;
    --card-top: #ffffff;
    --card-bottom: #e9d5dd;
    --brand-maroon: #8c2d48;
    --ink: #3a3a3a;
    --card-edge: #e2d4da;
    --decor-tone: #f1e3e8;
  }
  * { box-sizing: border-box; margin: 0; padding: 0; }
  html, body {
    width: 1200px;
    height: 900px;
    overflow: hidden;
    background: var(--page-bg);
  }
  .canvas {
    position: relative;
    width: 1200px;
    height: 900px;
  }
  .business-card {
    position: absolute;
    left: 424px;
    top: 135px;
    width: 352px;
    height: 630px;
    border-radius: 22px;
    border: 1px solid var(--card-edge);
    background: linear-gradient(180deg, var(--card-top) 0%, var(--card-top) 40%, var(--card-bottom) 100%);
    font-family: "Jura", sans-serif;
    overflow: hidden;
  }
  .background-decoration {
    position: absolute;
    left: 18px;
    top: 236px;
    width: 316px;
    height: 290px;
    border-radius: 18px;
    background: linear-gradient(180deg, var(--decor-tone) 0%, rgba(241, 227, 232, 0) 100%);
  }
  .brand {
    position: absolute;
    left: 0;
    right: 0;
    top: 128px;
    display: flex;
    align-items: center;
    justify-content: center;
    gap: 10px;
  }
  .brand-dot {
    width: 18px;
    height: 18px;
    border-radius: 50%;
    background: var(--brand-maroon);
  }
  .brand-name {
    font-size: 32px;
    font-weight: 500;
    color: var(--brand-maroon);
    text-transform: uppercase;
    white-space: nowrap;
  }
  .company-address {
    position: absolute;
    left: 24px;
    top: 392px;
    font-style: normal;
    font-size: 20px;
    line-height: 26px;
    color: var(--ink);
  }
  .contact-list {
    position: absolute;
    right: 24px;
    top: 512px;
    list-style: none;
    text-align: right;
    font-size: 19px;
    line-height: 25px;
    color: var(--brand-maroon);
    white-space: nowrap;
  }
</style>
</head>
<body>
  <main class="canvas">
    <article class="business-card">
      <div class="background-decoration" role="img" aria-label="Faint background decoration area"></div>

      <header class="brand">
        <span class="brand-dot" aria-hidden="true"></span>
        <span class="brand-name">Valtrion Tools</span>
      </header>

      <address class="company-address">
        Valtrion Tools Pte Ltd<br>
        27 Kallang Way #03-12,<br>
        Meridian Industrial Hub,<br>
        Singapore 349281
      </address>

      <ul class="contact-list">
        <li>Tel: 65-61234570</li>
        <li>Fax: 65-61234571</li>
        <li>Email: info@valtrion.com.sg</li>
      </ul>
    </article>
  </main>
</body>
</html>
```